IT Company needs stationary design

Business cards, MS Word, PowerPoint, A4 notepad design base on our company logo. This must be a set of templates in the same style which could be used both for printable documents as well as for documents shared digitally via email, website etc. This should be a modern design which is still professional, so make sure content is well readable both in MS Word and MS PowerPoint templates.
Updates

Target Market(s)

SME and Corporate

Industry/Entity Type

It Company

Font styles to use
Sans Serif

Colors
0455a3
0692cd
f37122
ffc214

Requirements
Must have
• 1) Business cards design: modern but still professional
• 2) MS Word: mostly for IT project documents (business analysis, reports, specifications, etc.) must be professional and easy readable.
• 3) MS PowerPoint: first slide, normal slide, last slide.
• 4) A4 notepad: header (must), footer (must), some light design on the background (optionally)
Nice to have
• Business cards design: would be nice to have 2-4 color variations of the same design from one side - cover (for example part of the cards are blue, part of the cards are orange) and other side with contact details is identical.

```html
<!DOCTYPE html>
<html lang="en">
<head>
<meta charset="utf-8">
<title>Nodevale Business Card</title>
<link rel="stylesheet" href="https://fonts.googleapis.com/css2?family=Quicksand:wght@500;600;700&display=swap">
<style>
  :root {
    --backdrop: #e4e4e2;
    --card-dark: #0a0a0a;
    --card-light: #f7f7f5;
    --brand-orange: #f37122;
    --brand-blue: #0692cd;
    --ink: #111111;
    --logo-light: #f4f4f4;
  }
  html, body {
    margin: 0;
    padding: 0;
    width: 1200px;
    height: 902px;
    overflow: hidden;
    background: var(--backdrop);
    font-family: "Quicksand", sans-serif;
  }
  .canvas {
    position: relative;
    width: 1200px;
    height: 902px;
  }
  .card {
    position: absolute;
    left: 340px;
    width: 520px;
    height: 297px;
    overflow: hidden;
    box-shadow: 0 6px 18px rgba(0,0,0,0.18);
  }
  .card-cover {
    top: 112px;
    background: var(--card-dark);
    display: flex;
    align-items: center;
    justify-content: center;
  }
  .brand {
    display: flex;
    align-items: center;
    gap: 14px;
    margin-top: -22px;
  }
  .brand-dot {
    width: 34px;
    height: 34px;
    border: 3px solid var(--logo-light);
    border-radius: 50%;
    box-sizing: border-box;
  }
  .brand-name {
    color: var(--logo-light);
    font-weight: 500;
    font-size: 30px;
    letter-spacing: 1px;
  }
  .card-contact {
    top: 470px;
    background: var(--card-light);
  }
  .accent-area {
    position: absolute;
    right: 0;
    top: 0;
    width: 150px;
    height: 297px;
    background: linear-gradient(180deg, rgba(243,113,34,0.85) 0%, rgba(243,113,34,0.35) 45%, rgba(6,146,205,0.35) 55%, rgba(6,146,205,0.85) 100%);
  }
  .holder {
    position: absolute;
    left: 24px;
    top: 20px;
    line-height: 1.05;
  }
  .holder-name {
    margin: 0;
    color: var(--brand-orange);
    font-weight: 600;
    font-size: 20px;
  }
  .holder-role {
    margin: 0;
    color: var(--brand-blue);
    font-weight: 600;
    font-size: 20px;
  }
  .contact-list {
    position: absolute;
    left: 24px;
    top: 128px;
    margin: 0;
    padding: 0;
    list-style: none;
    color: var(--ink);
    font-weight: 600;
    font-size: 15.5px;
    line-height: 25px;
  }
  .contact-list .web { color: #2a2a2a; }
</style>
</head>
<body>
<main class="canvas">
  <section class="card card-cover" aria-label="Card cover">
    <div class="brand">
      <span class="brand-dot"></span>
      <span class="brand-name">nodevale</span>
    </div>
  </section>

  <section class="card card-contact" aria-label="Card contact side">
    <div class="accent-area" role="img" aria-label="Decorative graphic in orange and blue belongs here"></div>
    <div class="holder">
      <p class="holder-name">Mr. Your Name</p>
      <p class="holder-role">Designation</p>
    </div>
    <ul class="contact-list">
      <li>Address line 1, Address line 2</li>
      <li>Phone : 0480 5516, Fax : 0480 5516</li>
      <li>Email : info@nodevale.com</li>
      <li class="web">Website : nodevale.com</li>
    </ul>
  </section>
</main>
</body>
</html>
```